Mellow Truffles. We need a website as delcious as our chocolate.

I need a website to promote our humble chocolate business. We our proud of are chocolate because we use only our favorite ingredients. We believe in originality and complete enjoyment of our chocolates. I am looking for a sleek and smooth website. I would like to see typical pages such as contact information and an intro. I would like to have a product page, which can be easily updated with photos of new chocolate. I would also like to see a page where we can educate customers about chocolate. This might be tricky but I would like our customers to leave the site knowing they are getting great chocolate! I have a logo and general color scheme, which I will try to upload somewhere. I looking for an original and exciting website.
Updates

Websites we like:

1. http://www.paul-van-orlen.example/ (looks really good)

2. http://www.tremilcocoa.example/

uploaded logo !

Target Market(s)

People who enjoy chocolate.

Industry/Entity Type

Business

Requirements
Must have
• User Friendly
Page were pictures of new chocolate can be easily updated.

Nice to have
• Calming and appetizing music
Section where recent tweets can show up on the site.

```html
<!DOCTYPE html>
<html lang="en">
<head>
<meta charset="utf-8">
<title>Mellow Truffles</title>
<link href="https://fonts.googleapis.com/css2?family=Lobster&family=Great+Vibes&family=Kalam:wght@400;700&display=swap" rel="stylesheet">
<style>
:root{
  --pink:#ffcccf;
  --pink-deep:#f7b3b9;
  --cream:#fcf8ea;
  --brown:#6e3f2b;
  --brown-dark:#4b2616;
  --brown-mid:#7d4530;
  --tan:#f4d9a9;
  --ribbon-dark:#b80d2a;
  --crimson:#d8173d;
  --teal:#14948f;
  --text:#4a2a1a;
  --link:#d0021b;
}
*{box-sizing:border-box;margin:0;padding:0}
html,body{width:1200px;height:1113px;overflow:hidden;background:#fff}
body{position:relative;font-family:Arial, Helvetica, sans-serif;color:var(--text)}

.top-band{position:absolute;left:0;top:0;width:1200px;height:56px;background:var(--pink);z-index:2}
.cart{position:absolute;right:68px;top:16px;display:flex;align-items:center;gap:8px;
  font-family:Kalam, cursive;font-size:19px;color:var(--brown)}

.hero{position:absolute;left:0;top:56px;width:1200px;height:542px;background:var(--cream)}

.main-nav{position:absolute;left:146px;top:108px;display:flex;gap:12px;z-index:3}
.main-nav a{width:118px;height:77px;display:flex;align-items:flex-end;justify-content:center;padding-bottom:18px;
  border-radius:50% 50% 0 0/44px 44px 0 0;background:linear-gradient(#7a4a35,#5c3322);
  color:#fff;font-family:Kalam, cursive;font-size:19px;text-decoration:none;white-space:nowrap}
.main-nav a.is-active{background:linear-gradient(#ffe0e2,var(--pink-deep));color:var(--brown);
  border:3px solid #fff;border-bottom:4px solid #3e2014;box-shadow:0 2px 3px rgba(0,0,0,.3)}

.search{position:absolute;left:838px;top:147px;display:flex;gap:6px;z-index:3}
.search input{width:166px;height:30px;border:0;border-radius:4px;background:var(--brown);
  color:#fff;font:15px Arial, sans-serif;padding:4px 8px}
.search input::placeholder{color:#fff}
.search button{width:54px;height:30px;border:0;border-radius:5px;background:var(--brown);color:#fff;font:16px Arial, sans-serif}

.slider{position:absolute;left:103px;top:196px;width:1005px;height:349px;background:#fff;padding:6px;
  box-shadow:0 4px 8px rgba(0,0,0,.3);display:flex;z-index:2}
.slide-brand{position:relative;width:279px;height:100%;background:#6b3517;overflow:hidden}
.slide-brand .name{position:absolute;top:40px;left:0;width:100%;text-align:center;
  font-family:Lobster, cursive;font-size:28px;color:#c2469a}
.slide-brand .art{position:absolute;left:0;top:96px;width:279px;height:241px;
  background:linear-gradient(135deg,#8c3f86,#6b3517)}
.slide-photo{flex:1;background:linear-gradient(135deg,#3a1b0e,#6a3a22 55%,#2e150a)}
.slider-frame{position:absolute;left:103px;top:196px;width:1005px;height:349px;overflow:hidden;z-index:3;pointer-events:none}
.learn-more{position:absolute;right:-20px;top:18px;width:150px;height:34px;background:linear-gradient(#f9b3bd,#f28d9c);
  transform:rotate(45deg);text-align:center;font-family:Kalam, cursive;font-size:19px;line-height:34px;color:var(--brown-dark);
  box-shadow:0 2px 3px rgba(0,0,0,.25)}
.arrow{position:absolute;top:436px;width:28px;height:54px;z-index:4}
.arrow.prev{left:86px}
.arrow.next{left:1096px}

.tagline{position:absolute;left:0;top:598px;width:1200px;height:62px;background:var(--pink);
  font-family:"Great Vibes", cursive;font-size:31px;color:var(--crimson);text-align:center;line-height:64px}

.features{position:absolute;left:0;top:660px;width:1200px;height:357px;
  background:linear-gradient(var(--brown-mid),#5b301d)}
.card{position:absolute;top:61px;width:279px;height:244px;background:var(--tan);
  box-shadow:0 6px 10px rgba(0,0,0,.35);padding:80px 12px 0 11px}
.card:nth-child(1){left:132px}
.card:nth-child(2){left:461px}
.card:nth-child(3){left:790px}
.ribbon{position:absolute;left:-18px;top:15px;width:315px;height:40px;background:linear-gradient(#f0304f,var(--ribbon-dark));
  font-family:Lobster, cursive;font-size:23px;font-weight:400;color:#ffe9cf;padding:6px 0 0 42px;
  clip-path:polygon(0 0,100% 0,96% 50%,100% 100%,0 100%,4% 50%)}
.treat{position:absolute;right:24px;top:-6px;width:48px;height:56px;border-radius:6px;
  background:linear-gradient(#f6c9d0,#a0634a)}
.card p{font-size:14.5px;line-height:20.5px;text-align:justify}
.card p .hl{color:var(--link)}
.card .cta{position:absolute;left:12px;top:193px;font-family:Lobster, cursive;font-size:20px;color:var(--teal);white-space:nowrap}

.site-footer{position:absolute;left:0;top:1017px;width:1200px;height:53px;background:var(--pink)}
.copyright{position:absolute;left:107px;top:25px;font-size:14px;color:#222}
.social{position:absolute;left:1006px;top:7px;display:flex;gap:14px}
.social span{width:36px;height:36px;border-radius:50%;background:var(--brown)}
</style>
</head>
<body>
<header class="top-band">
  <div class="cart">Shopping Cart
    <svg width="28" height="24" viewBox="0 0 28 24" fill="none" stroke="#6e3f2b" stroke-width="2.4" stroke-linejoin="round">
      <path d="M1 3h5l3 12h14l3-9H8"/><circle cx="11" cy="20" r="2" fill="#6e3f2b"/><circle cx="21" cy="20" r="2" fill="#6e3f2b"/>
    </svg>
  </div>
</header>

<section class="hero" role="img" aria-label="Cream background with soft vertical stripes"></section>

<nav class="main-nav">
  <a href="#" class="is-active">Home</a>
  <a href="#">Our Product</a>
  <a href="#">Oline Shop</a>
  <a href="#">About us</a>
  <a href="#">Contact Us</a>
</nav>

<form class="search">
  <input type="text" placeholder="Search...">
  <button type="button">Go</button>
</form>

<div class="slider">
  <div class="slide-brand">
    <div class="name">Mellow Truffles</div>
    <div class="art" role="img" aria-label="Decorative purple tree illustration"></div>
  </div>
  <div class="slide-photo" role="img" aria-label="Close-up photograph of assorted chocolate truffles and white coconut pralines"></div>
</div>
<div class="slider-frame"><div class="learn-more">learn more</div></div>

<svg class="arrow prev" viewBox="0 0 28 54"><path d="M28 0C10 6 0 16 0 27s10 21 28 27Z" fill="#b9b2ae"/><path d="M17 19l-8 8 8 8" stroke="#fff" stroke-width="3" fill="none"/></svg>
<svg class="arrow next" viewBox="0 0 28 54"><path d="M0 0c18 6 28 16 28 27S18 48 0 54Z" fill="#b9b2ae"/><path d="M11 19l8 8-8 8" stroke="#fff" stroke-width="3" fill="none"/></svg>

<div class="tagline">Mellow Truffles Offers the Finest Baked Treats and Candy Anywhere in the World</div>

<section class="features">
  <article class="card">
    <h2 class="ribbon">Deliciousness</h2>
    <div class="treat" role="img" aria-label="Small layered cake illustration"></div>
    <p>Quisque posuere ligula sit amet massa accumsan id rutrum lectus suscipit. Donec in neque mauris, non pulvinar quam. Donec felis ante, placerat eu feugiat non, sagittis eu magna.</p>
    <a class="cta">Shop for pure flavor heaven now</a>
  </article>
  <article class="card">
    <h2 class="ribbon">Get it Fresh</h2>
    <div class="treat" role="img" aria-label="Small cherry cake illustration"></div>
    <p>Vivamus ac nisi eros, eget semper purus. Sed ullamcorper, <span class="hl">augue quis feugiat tincidunt, erat felis</span> consectetur nibh, a hendrerit eros felis eu dui.</p>
    <a class="cta">Order fresh baked goods now</a>
  </article>
  <article class="card">
    <h2 class="ribbon">Flavorific</h2>
    <div class="treat" role="img" aria-label="Small cupcake illustration"></div>
    <p>Lorem ipsum dolor sit amet, consectetur adipiscing elit. Integer odio nisl, vulputate vel blandit nec, <span class="hl">congue a sem</span>. Aenean dapibus sagittis lectus id vehicula. Quist magnust nec lectus.</p>
    <a class="cta">We use the freshest of ingredients</a>
  </article>
</section>

<footer class="site-footer">
  <div class="copyright">Copyright © 2012 Mellow Truffles</div>
  <div class="social" aria-label="Social links"><span></span><span></span></div>
</footer>
</body>
</html>
```